Laundromat Grand Opening.

Laundromat /Grand opening. One side English, one side Spanish. Include the Address, Name, Raffle/Prizes and Grand opening date.
Elmridge Wash Laundromat, 415 W. Harlan Ave. 2/7/2016. (555) 314-2297.

Coin

000000

• Eye catching. Laundry theme.

```html
<!DOCTYPE html>
<html lang="en">
<head>
<meta charset="utf-8">
<title>Elmridge Wash Laundromat – Grand Opening</title>
<link rel="stylesheet" href="https://fonts.googleapis.com/css2?family=Oswald:wght@700&family=Bebas+Neue&family=Lato:wght@400;700&family=Roboto:wght@700&display=swap">
<style>
  :root {
    --backdrop: #e6e6e6;
    --ink: #0b0b0b;
    --white: #f4f4f4;
    --brand-blue: #3d77c3;
    --card-light: #f3f3f3;
    --card-shade: #d9d9d9;
    --steel-light: #dfe4ea;
    --steel-mid: #9aa6b4;
    --steel-dark: #4a5563;
  }
  html, body {
    margin: 0;
    padding: 0;
    width: 1200px;
    height: 888px;
    overflow: hidden;
    background: var(--backdrop);
  }
  .canvas {
    position: relative;
    width: 1200px;
    height: 888px;
  }
  .flyer-shapes {
    position: absolute;
    inset: 0;
  }
  .headline {
    position: absolute;
    margin: 0;
    font-family: "Oswald", "Arial Narrow", sans-serif;
    font-weight: 700;
    line-height: 1;
    text-align: center;
    left: 688px;
    width: 420px;
    white-space: nowrap;
    transform-origin: center top;
  }
  .headline-grand {
    top: 81px;
    font-size: 150px;
    color: var(--white);
    letter-spacing: -1px;
    transform: scaleX(0.92);
  }
  .headline-opening {
    top: 247px;
    font-size: 108px;
    color: var(--brand-blue);
    letter-spacing: -1px;
    transform: scaleX(0.97);
  }
  .event-date, .event-time {
    position: absolute;
    margin: 0;
    font-family: "Bebas Neue", "Arial Narrow", sans-serif;
    color: var(--ink);
    line-height: 1;
    width: 440px;
    text-align: center;
    white-space: nowrap;
    transform-origin: center top;
  }
  .event-date {
    left: 589px;
    top: 478px;
    font-size: 96px;
    letter-spacing: 1px;
    transform: scaleX(0.85);
  }
  .event-time {
    left: 603px;
    top: 584px;
    font-size: 48px;
  }
  .raffle-badge {
    position: absolute;
    left: 142px;
    top: 556px;
    width: 240px;
    margin: 0;
    font-family: "Roboto", Arial, sans-serif;
    font-weight: 700;
    font-size: 72px;
    line-height: 80px;
    color: var(--brand-blue);
    text-align: center;
  }
  .venue-box {
    position: absolute;
    left: 440px;
    top: 650px;
    width: 693px;
    height: 137px;
    background: var(--brand-blue);
    border-radius: 14px 0 0 14px;
    font-family: "Lato", Arial, sans-serif;
    box-sizing: border-box;
    padding: 18px 0 0 0;
    text-align: center;
  }
  .venue-name {
    margin: 0;
    font-weight: 700;
    font-size: 38px;
    color: var(--white);
    line-height: 1.1;
  }
  .venue-address {
    margin: 8px 0 0;
    font-weight: 400;
    font-size: 44px;
    color: var(--ink);
    line-height: 1.1;
  }
</style>
</head>
<body>
<main class="canvas">
  <svg class="flyer-shapes" width="1200" height="888" viewBox="0 0 1200 888">
    <defs>
      <linearGradient id="card-fill" x1="0" y1="0" x2="1" y2="1">
        <stop offset="0" stop-color="#f3f3f3"/>
        <stop offset="1" stop-color="#d9d9d9"/>
      </linearGradient>
      <linearGradient id="washer-fill" x1="0" y1="0" x2="1" y2="1">
        <stop offset="0" stop-color="#dfe4ea"/>
        <stop offset="0.5" stop-color="#9aa6b4"/>
        <stop offset="1" stop-color="#4a5563"/>
      </linearGradient>
    </defs>

    <rect class="card" x="68" y="82" width="1065" height="722" fill="url(#card-fill)"/>

    <path class="black-panel" d="M640 82 H1133 V492 C1060 440 920 402 780 402 C710 402 660 414 625 430 C670 330 680 200 640 82 Z" fill="var(--ink)"/>
    <path class="black-panel-edge" d="M625 430 C660 414 710 402 780 402 C920 402 1060 440 1133 492" fill="none" stroke="var(--brand-blue)" stroke-width="12"/>

    <path class="washer-photo" role="img" aria-label="Photo of front-loading stainless steel washing machines in a laundromat"
          d="M68 82 H655 C700 210 690 390 560 500 C480 570 420 610 370 628 L68 640 Z" fill="url(#washer-fill)"/>
    <path class="washer-photo-edge" d="M655 82 C700 210 690 390 560 500 C480 570 420 610 370 628" fill="none" stroke="var(--brand-blue)" stroke-width="9"/>
    <path class="lower-wave" d="M68 636 C180 632 300 628 380 624 C300 650 180 664 68 670 Z" fill="var(--brand-blue)"/>

    <g class="raffle-star" fill="var(--ink)">
      <rect x="147" y="517" width="230" height="230" transform="rotate(0 262 632)"/>
      <rect x="147" y="517" width="230" height="230" transform="rotate(11.25 262 632)"/>
      <rect x="147" y="517" width="230" height="230" transform="rotate(22.5 262 632)"/>
      <rect x="147" y="517" width="230" height="230" transform="rotate(33.75 262 632)"/>
      <rect x="147" y="517" width="230" height="230" transform="rotate(45 262 632)"/>
      <rect x="147" y="517" width="230" height="230" transform="rotate(56.25 262 632)"/>
      <rect x="147" y="517" width="230" height="230" transform="rotate(67.5 262 632)"/>
      <rect x="147" y="517" width="230" height="230" transform="rotate(78.75 262 632)"/>
    </g>
  </svg>

  <h1 class="headline headline-grand">GRAND</h1>
  <h2 class="headline headline-opening">OPENING</h2>

  <p class="event-date">FEB 7TH. 2016</p>
  <p class="event-time">TIME 7:00 A.M TILL 10:00P.M.</p>

  <p class="raffle-badge">Raffle<br>Prizes</p>

  <div class="venue-box">
    <p class="venue-name">ELMRIDGE WASH LAUNDROMAT</p>
    <p class="venue-address">415 W. Harlan Ave. 2/7/2016</p>
  </div>
</main>
</body>
</html>
```